Advertisement Sign Project

Hi there,

I have a commercial space available for short term lease.

I need an advertisement sign to go on the double black doors (under the current Bornavel Quindrex sign).

The advertising sign should be about A3 in size and designed to attract pedestrians.

See site address at 417 Calder Parade Richmond Victoria Australia:

https://plotfinder.example-atlas.com.au/view?q=417B+Calder+Pde,+Richmond+Victoria+3121&z=17

Target Market(s)

Pop-up store tenants: fashion, textiles, bedding, furniture, homewares and kitchenwares.

The photos are provided to give you (the graphic designer) an idea of the space available.

Requirements
Must have
• Retail tenancy available for short term lease.

For all enquiries contact Owen - 0412730648 or email owen@calderparadehub.com.au

Nice to have
• Something befitting the look and feel of the building.

I was thinking a textile pattern as background, or some kind of fashion design element to inspire a potential pop up shop tenant.

```html
<!DOCTYPE html>
<html lang="en">
<head>
<meta charset="utf-8">
<title>Retail Tenancy – Short Term Lease</title>
<link rel="stylesheet" href="https://fonts.googleapis.com/css2?family=Alfa+Slab+One&family=Barlow+Condensed:wght@500;600&display=swap">
<style>
  :root {
    --frame: #070a10;
    --navy: #1c4a86;
    --stitch: #9fb4d2;
    --gold: #f3c51a;
    --paper: #f1f1f1;
    --ink: #10151f;
    --ornament: #d9dcdf;
  }
  html, body {
    margin: 0;
    padding: 0;
    width: 848px;
    height: 1200px;
    overflow: hidden;
    background: var(--frame);
  }
  .sign {
    position: relative;
    width: 848px;
    height: 1200px;
    background: var(--frame);
  }
  .sign__panel {
    position: absolute;
    inset: 6px;
    background: var(--navy);
    border-radius: 4px;
  }
  .sign__stitch {
    position: absolute;
    inset: 14px;
    border: 1.5px dashed var(--stitch);
    border-radius: 3px;
  }
  .ornament {
    position: absolute;
    background: var(--ornament);
    border-radius: 40% 40% 50% 50%;
    opacity: 0.9;
  }
  .ornament--crest { left: 340px; top: 58px; width: 172px; height: 182px; }
  .ornament--divider { left: 374px; top: 600px; width: 98px; height: 96px; }
  .sign__type {
    position: absolute;
    inset: 0;
  }
  .headline {
    font-family: "Alfa Slab One", Georgia, serif;
    fill: var(--gold);
    stroke: var(--ink);
    stroke-width: 9;
    paint-order: stroke fill;
    stroke-linejoin: round;
  }
  .subhead {
    font-family: "Alfa Slab One", Georgia, serif;
    fill: var(--paper);
    stroke: var(--ink);
    stroke-width: 6;
    paint-order: stroke fill;
    stroke-linejoin: round;
  }
  .contact-line {
    font-family: "Barlow Condensed", "Arial Narrow", sans-serif;
    font-weight: 500;
    fill: var(--gold);
    stroke: var(--ink);
    stroke-width: 3;
    paint-order: stroke fill;
  }
  .phone-number {
    font-family: "Barlow Condensed", "Arial Narrow", sans-serif;
    font-weight: 600;
    fill: var(--paper);
    stroke: var(--ink);
    stroke-width: 7;
    paint-order: stroke fill;
    stroke-linejoin: round;
  }
  .phone-icon { fill: var(--paper); stroke: var(--ink); stroke-width: 5; paint-order: stroke fill; }
  .phone-icon__dial { fill: var(--navy); }
</style>
</head>
<body>
<main class="sign">
  <div class="sign__panel"></div>
  <div class="sign__stitch"></div>

  <div class="ornament ornament--crest" role="img" aria-label="Fleur-de-lis ornament"></div>
  <div class="ornament ornament--divider" role="img" aria-label="Small fleur-de-lis divider ornament"></div>

  <svg class="sign__type" viewBox="0 0 848 1200" width="848" height="1200">
    <text class="headline" x="424" y="408" text-anchor="middle" font-size="158" textLength="536" lengthAdjust="spacingAndGlyphs">RETAIL</text>
    <text class="headline" x="430" y="556" text-anchor="middle" font-size="158" textLength="658" lengthAdjust="spacingAndGlyphs">TENANCY</text>

    <text class="subhead" x="424" y="787" text-anchor="middle" font-size="64" textLength="322" lengthAdjust="spacingAndGlyphs">AVAILABLE</text>
    <text class="subhead" x="424" y="862" text-anchor="middle" font-size="64" textLength="724" lengthAdjust="spacingAndGlyphs">FOR SHORT TERM LEASE</text>

    <text class="contact-line" x="424" y="945" text-anchor="middle" font-size="48" textLength="584" lengthAdjust="spacingAndGlyphs">FOR ALL ENQUIRIES CONTACT OWEN</text>

    <g class="phone-icon" aria-hidden="true">
      <path d="M114 1008 C114 978 232 978 234 1008 L234 1020 C234 1026 208 1026 206 1020 L204 1008 C196 1000 152 1000 144 1008 L142 1020 C140 1026 114 1026 114 1020 Z"/>
      <path d="M150 1012 L198 1012 L226 1044 L226 1066 L122 1066 L122 1044 Z"/>
      <circle class="phone-icon__dial" cx="174" cy="1040" r="14" stroke="none"/>
    </g>
    <text class="phone-number" x="500" y="1064" text-anchor="middle" font-size="118" textLength="474" lengthAdjust="spacingAndGlyphs">0412730648</text>

    <text class="contact-line" x="424" y="1131" text-anchor="middle" font-size="38" textLength="468" lengthAdjust="spacingAndGlyphs">OWEN@CALDERPARADEHUB.COM.AU</text>
  </svg>
</main>
</body>
</html>
```